Pregnancy and Fertility Information Website

Hello Designers,
I need a website which provide tips and information about healthy and happy pregnancy. My website name is Lorvin medical.

The website should provide all the information needed throughout pregnancy and beyond ranging from pregnancy tracking tools and articles about common pregnancy concerns and what to expect during pregnancy,etc.
The details about first trimester, second trimester and third trimester should be highlighted in the website.

Top Navigation
Home, Fertility, Pregnancy basics, Articles, Tips and News

I'm looking for a simple and clean design which involves captivating images and colors but it shouldn't be crowded. The design must be professional and modern. An easy to navigate layout is a must.

Green, violet, blue and light yellow colors are my favorites but i'm open to other options.

Any questions. Kindly ask

Industry/Entity Type

Medical

```html
<!DOCTYPE html>
<html lang="en">
<head>
<meta charset="utf-8">
<title>Lorvin Medical – Care During Pregnancy</title>
<link rel="stylesheet" href="https://fonts.googleapis.com/css2?family=Open+Sans:wght@300;400;600;700&display=swap">
<style>
  :root {
    --blue: #1e73be;
    --blue-dark: #195fa0;
    --blue-nav: #2a86d0;
    --green: #4caf50;
    --green-btn: #66bb6a;
    --violet: #7a1fd1;
    --violet-deep: #5a12b8;
    --yellow: #fbc22a;
    --ink: #1d1d1d;
    --text: #333;
    --muted: #777;
    --panel: #e4e4e4;
    --white: #fff;
  }
  * { margin: 0; padding: 0; box-sizing: border-box; }
  html, body { width: 1200px; height: 2222px; overflow: hidden; background: var(--white); }
  body { font-family: "Open Sans", Arial, sans-serif; color: var(--text); position: relative; }
  .abs { position: absolute; }

  /* header */
  .brand { left: 108px; top: 40px; display: flex; align-items: center; gap: 12px; }
  .brand-dot { width: 44px; height: 44px; border-radius: 50%; background: var(--blue); }
  .brand-name { font-size: 26px; font-weight: 600; color: var(--blue); }
  .call { left: 855px; top: 43px; display: flex; align-items: center; gap: 12px; font-size: 19px; color: var(--blue); }
  .call-icon { width: 32px; height: 32px; border-radius: 50%; background: var(--green); display: flex; align-items: center; justify-content: center; }

  .nav { left: 100px; top: 124px; width: 1015px; height: 46px; background: linear-gradient(var(--blue-nav), var(--blue-dark)); display: flex; align-items: center; padding-left: 37px; }
  .nav a { color: var(--white); text-decoration: none; font-size: 15px; margin-right: 30px; }
  .nav .search { position: absolute; right: 24px; top: 14px; }

  /* hero */
  .hero { left: 100px; top: 170px; width: 1015px; height: 544px; background: linear-gradient(90deg, #dfe2f7 0%, #eceefa 45%, #f3f3f8 100%); overflow: hidden; }
  .hero-photo { position: absolute; left: 500px; top: 0; width: 515px; height: 544px; background: radial-gradient(ellipse at 55% 50%, #e9d6cf 0%, #efe6ea 35%, #f2f1f7 70%); }
  .hero-title { position: absolute; left: 83px; top: 192px; font-size: 36px; line-height: 42px; color: var(--ink); font-weight: 400; }
  .hero-title b { font-weight: 700; }
  .hero-title .g { color: var(--green); font-weight: 600; }
  .hero-title .v { color: var(--violet); font-weight: 700; }
  .btn { display: inline-block; background: linear-gradient(#2f86d2, var(--blue-dark)); color: var(--white); font-weight: 700; text-transform: uppercase; text-align: center; border-radius: 2px; }
  .hero-btn { position: absolute; left: 88px; top: 349px; width: 136px; height: 44px; line-height: 44px; font-size: 15px; }
  .dots { position: absolute; left: 80px; top: 497px; display: flex; gap: 17px; }
  .dots span { width: 10px; height: 10px; border-radius: 50%; background: var(--white); }
  .dots .on { background: var(--blue); }

  /* welcome */
  .welcome { left: 0; top: 736px; width: 1200px; text-align: center; }
  .welcome h1 { font-size: 29px; font-weight: 300; color: var(--ink); letter-spacing: 0.5px; }
  .welcome h1 b { font-weight: 700; }
  .welcome .sub { margin-top: 10px; font-size: 21px; font-weight: 300; display: flex; justify-content: center; align-items: center; gap: 14px; color: var(--text); }
  .welcome .sub::before, .welcome .sub::after { content: ""; width: 70px; border-top: 1px solid #666; }
  .welcome p { width: 740px; margin: 18px auto 0; font-size: 13.5px; line-height: 22px; color: var(--ink); }
  .welcome .btn { margin-top: 22px; width: 99px; height: 31px; line-height: 31px; font-size: 11px; }

  /* trimester */
  .video { left: 115px; top: 980px; width: 512px; height: 338px; background: var(--panel); }
  .video-art { position: absolute; left: 0; top: 0; width: 512px; height: 338px; background: linear-gradient(#e6e6e6, #dcdcdc); }
  .play { position: absolute; left: 219px; top: 106px; }
  .stages { position: absolute; left: 29px; top: 258px; display: flex; gap: 5px; }
  .stages span { width: 106px; height: 30px; line-height: 30px; text-align: center; color: var(--white); font-size: 16px; font-weight: 600; background: #b0b0b0; border: 1px solid #9a9a9a; border-radius: 3px; }
  .stages span:nth-child(2) { background: #a3a3a3; }
  .stages span:nth-child(3) { background: #8c8c8c; }
  .stages span:nth-child(4) { background: #5c5c5c; }
  .details { left: 655px; top: 1028px; width: 445px; }
  .details h2 { font-size: 24px; font-weight: 300; color: var(--ink); }
  .details h2 b { font-weight: 700; }
  .details p { margin-top: 14px; font-size: 12.5px; line-height: 21px; text-align: justify; color: var(--ink); }
  .details p + p { margin-top: 21px; }
  .details .btn { margin-top: 33px; width: 99px; height: 31px; line-height: 31px; font-size: 11px; }

  /* articles */
  .popular { left: 126px; top: 1366px; }
  .popular h2 { font-size: 24px; font-weight: 300; line-height: 42px; color: var(--ink); }
  .popular h2 b { font-weight: 700; }
  .popular ul { list-style: none; margin-top: 24px; }
  .popular li { display: flex; align-items: center; gap: 10px; height: 31.5px; font-size: 14.5px; color: var(--ink); padding-left: 4px; }
  .card { top: 1374px; width: 328px; }
  .card-img { width: 328px; height: 151px; }
  .card h3 { margin-top: 17px; font-size: 20px; font-weight: 400; color: var(--ink); }
  .card p { margin-top: 12px; font-size: 12.5px; line-height: 21px; text-align: justify; color: var(--ink); }
  .card .btn { margin-top: 24px; width: 99px; height: 32px; line-height: 32px; font-size: 11px; }

  /* calendar banner */
  .calendar { left: 100px; top: 1740px; width: 1015px; height: 304px; background: #f6f7f9; overflow: hidden; }
  .calendar-photo { position: absolute; left: 545px; top: 0; width: 470px; height: 304px; background: linear-gradient(90deg, #f6f7f9 0%, #ece7e2 40%, #d9c8b8 75%, #ece8e4 100%); }
  .calendar .new { position: absolute; left: 62px; top: 38px; font-size: 63px; line-height: 70px; color: var(--violet-deep); }
  .calendar .mom { position: absolute; left: 62px; top: 114px; background: var(--yellow); color: var(--white); font-size: 55px; line-height: 52px; padding: 0 2px; }
  .calendar .download { position: absolute; left: 62px; top: 190px; width: 158px; height: 35px; line-height: 35px; font-size: 13px; font-weight: 700; color: var(--white); text-align: center; background: linear-gradient(#77c77a, #56ad5a); border-radius: 2px; }

  /* footer */
  .foot-nav { left: 0; top: 2076px; width: 1200px; display: flex; justify-content: center; gap: 33px; font-size: 15px; color: var(--muted); }
  .social { left: 501px; top: 2121px; display: flex; gap: 14px; }
  .social span { width: 43px; height: 43px; border-radius: 50%; }
  .copy { left: 0; top: 2190px; width: 1200px; text-align: center; font-size: 14px; color: #555; }
</style>
</head>
<body>

<header>
  <div class="abs brand"><span class="brand-dot"></span><span class="brand-name">Lorvin medical</span></div>
  <div class="abs call">
    <span class="call-icon">
      <svg width="16" height="16" viewBox="0 0 24 24"><path fill="#fff" d="M6.6 10.8a15.1 15.1 0 0 0 6.6 6.6l2.2-2.2c.3-.3.7-.4 1-.2 1.1.4 2.3.6 3.6.6.6 0 1 .4 1 1V20c0 .6-.4 1-1 1A17 17 0 0 1 3 4c0-.6.4-1 1-1h3.5c.6 0 1 .4 1 1 0 1.3.2 2.5.6 3.6.1.3 0 .7-.2 1z"/></svg>
    </span>
    Call Us : 1-800 555 0142
  </div>
  <nav class="abs nav">
    <a href="#">Home</a><a href="#">Fertility</a><a href="#">Pregnancy basics</a><a href="#">Articles</a><a href="#">Tips and News</a><a href="#">Contact us</a>
    <svg class="search" width="16" height="16" viewBox="0 0 16 16"><circle cx="6.5" cy="6.5" r="4.5" fill="none" stroke="#fff" stroke-width="2"/><line x1="10" y1="10" x2="14" y2="14" stroke="#fff" stroke-width="2.4" stroke-linecap="round"/></svg>
  </nav>
</header>

<section class="abs hero">
  <div class="hero-photo" role="img" aria-label="Pregnant woman in a white draped gown holding a pink flower"></div>
  <h2 class="hero-title">We provide <b>tips and<br>information</b> about <span class="g">healthy</span><br>and <span class="v">happy pregnancy.</span></h2>
  <a class="btn hero-btn">Learn more</a>
  <div class="dots"><span></span><span></span><span></span><span class="on"></span></div>
</section>

<section class="abs welcome">
  <h1>WELCOME&nbsp; TO <b>LORVIN MEDICAL</b></h1>
  <div class="sub">Care During Pregnancy</div>
  <p>Asptaiades kertyaser daesraeds. Casrolern atur aut oditaut. Binsequuntur magni dolqui ratio volmsequi nesciu orbosas numquam eius modi teincidunt, ut labore et dolore magnam.</p>
  <a class="btn">Learn more</a>
</section>

<section>
  <div class="abs video">
    <div class="video-art" role="img" aria-label="Silhouettes of a woman through the three trimesters and holding her baby after birth"></div>
    <svg class="play" width="72" height="72" viewBox="0 0 72 72"><circle cx="36" cy="36" r="33" fill="none" stroke="#9a9a9a" stroke-width="3"/><path d="M29 23 L50 36 L29 49 Z" fill="none" stroke="#9a9a9a" stroke-width="3" stroke-linejoin="round"/></svg>
    <div class="stages"><span>1 Trimester</span><span>2 Trimester</span><span>3 Trimester</span><span>Birth</span></div>
  </div>
  <div class="abs details">
    <h2>THE DETAILS ABOUT <b>FIRST TRIMESTER...</b></h2>
    <p>Sesquam estqui dolorem ipsudolor sitamet conetasedas adipisci umquam eius. Basmodi tempora iduntut laborease dolore magnam aliqua quaerat ptatem. Munim ad minim eniamagse quis nostrum exercitationem ullam.</p>
    <p>Beciegast nveriti vitaesaert viasead asety kertya aset aplicaboserde miuas nerafae kertyerauas vitaesa ertyatya nemo eniptaiades</p>
    <a class="btn">Read more</a>
  </div>
</section>

<section>
  <div class="abs popular">
    <h2>POPULAR ARTICLES <b>&amp;<br>PUBLICATIONS</b></h2>
    <ul>
      <li><svg width="14" height="14" viewBox="0 0 14 14"><circle cx="7" cy="7" r="7" fill="#111"/><path d="M3.8 7.2 L6 9.3 L10.3 4.8" fill="none" stroke="#fff" stroke-width="1.8"/></svg>Vatsreasa</li>
      <li><svg width="14" height="14" viewBox="0 0 14 14"><circle cx="7" cy="7" r="7" fill="#111"/><path d="M3.8 7.2 L6 9.3 L10.3 4.8" fill="none" stroke="#fff" stroke-width="1.8"/></svg>Binsequuntur magni</li>
      <li><svg width="14" height="14" viewBox="0 0 14 14"><circle cx="7" cy="7" r="7" fill="#111"/><path d="M3.8 7.2 L6 9.3 L10.3 4.8" fill="none" stroke="#fff" stroke-width="1.8"/></svg>Casrolern atur</li>
      <li><svg width="14" height="14" viewBox="0 0 14 14"><circle cx="7" cy="7" r="7" fill="#111"/><path d="M3.8 7.2 L6 9.3 L10.3 4.8" fill="none" stroke="#fff" stroke-width="1.8"/></svg>Asptaiades</li>
      <li><svg width="14" height="14" viewBox="0 0 14 14"><circle cx="7" cy="7" r="7" fill="#111"/><path d="M3.8 7.2 L6 9.3 L10.3 4.8" fill="none" stroke="#fff" stroke-width="1.8"/></svg>Kertyaser daesraeds</li>
      <li><svg width="14" height="14" viewBox="0 0 14 14"><circle cx="7" cy="7" r="7" fill="#111"/><path d="M3.8 7.2 L6 9.3 L10.3 4.8" fill="none" stroke="#fff" stroke-width="1.8"/></svg>Binsequuntur magni</li>
      <li><svg width="14" height="14" viewBox="0 0 14 14"><circle cx="7" cy="7" r="7" fill="#111"/><path d="M3.8 7.2 L6 9.3 L10.3 4.8" fill="none" stroke="#fff" stroke-width="1.8"/></svg>Casrolern atur</li>
      <li><svg width="14" height="14" viewBox="0 0 14 14"><circle cx="7" cy="7" r="7" fill="#111"/><path d="M3.8 7.2 L6 9.3 L10.3 4.8" fill="none" stroke="#fff" stroke-width="1.8"/></svg>Asptaiades</li>
    </ul>
  </div>

  <article class="abs card" style="left:402px">
    <div class="card-img" role="img" aria-label="Young woman lying in bed smiling at a pregnancy test" style="background:linear-gradient(90deg,#e9ddd6,#d9b9a4 50%,#efe7e2)"></div>
    <h3>Newly Pregnancy experience</h3>
    <p>Nertyase riti masertas lertyars kuhas asety kertya aset aplicabo nerafaeskes kertyu ersvitae ertynemo lasec vaerat niptaiades goertayse</p>
    <a class="btn">Read more</a>
  </article>

  <article class="abs card" style="left:771px">
    <div class="card-img" role="img" aria-label="Pregnant woman in a bright kitchen holding a bowl of salad" style="background:linear-gradient(90deg,#e4e8e2,#f1ece6 45%,#dfe6d6)"></div>
    <h3>Healthy Food</h3>
    <p>Nertyase riti masertas lertyars kuhas asety kertya aset aplicabo nerafaeskes kertyu ersvitae ertynemo lasec vaerat niptaiades goertayse</p>
    <a class="btn">Read more</a>
  </article>
</section>

<section class="abs calendar">
  <div class="calendar-photo" role="img" aria-label="Pregnant woman in a beige cardigan by a curtained window"></div>
  <div class="new">New!</div>
  <div class="mom">Mom Calendar</div>
  <a class="download">DOWNLOAD NOW</a>
</section>

<footer>
  <div class="abs foot-nav"><span>Home</span><span>Fertility</span><span>Pregnancy basics</span><span>Articles</span><span>Tips and News</span><span>Contact us</span></div>
  <div class="abs social">
    <span style="background:#7ec8e8"></span>
    <span style="background:#f17c7c"></span>
    <span style="background:#5b73b5"></span>
    <span style="background:#f6cf6c"></span>
  </div>
  <div class="abs copy">© 2017. www.lorvinmedical.com</div>
</footer>

</body>
</html>
```